Fresh looking flyer for Vantrel Academy Of Computing

We need a flyer design for our IT school that will be distributed to potential students during our recruitment campaign. We want to feature the following aspects of the school:

-Study IT in a nordic/european way close to your home (design should feel Scandinavian)
-Featuring the dean of the school (photo attached)
-Match the theme of logo (logo attached)
-A potential layout attached as a mockup

CONTENT
* Main Message " LEARN EUROPEAN PROGRAMMING COURSES IN BEKASI"
* Sub Message " 3 MONTH MODULES FROM BEGINNER TO ADVANCED"
* Campaign " ATTEND FREE CLASS & GET 10% OFF COURSE, SIGN UP BETWEEN 7-18MARCH. vantrel.example/free
* Extra info: " GRADUATE AND GET HIRED TO EARN 120 MILLION IDR/YEAR"

End result should be in Adobe Illustrator format.

Target Market(s)

18-30 year old Indonesians interested in IT

Industry/Entity Type

Education

Font styles to use
Sans Serif

Colors
85cae6

Requirements
Must have
• -Photo of the manager
• -Messages as in the project description
• -School logo
• -Nordic look and feel

```html
<!DOCTYPE html>
<html lang="en">
<head>
<meta charset="utf-8">
<title>Vantrel Academy Of Computing – Flyer</title>
<link rel="stylesheet" href="https://fonts.googleapis.com/css2?family=Barlow+Semi+Condensed:wght@700&family=Lato:wght@400;700;900&display=swap">
<style>
  :root {
    --mat: #3d3d3f;
    --paper: #f4f5f7;
    --navy: #123e6e;
    --navy-fold: #0d2f56;
    --sky: #92c5e8;
    --slate: #404042;
    --white: #ffffff;
    --skin: #e7cdbd;
    --shirt: #f1f1f1;
  }
  * { margin: 0; padding: 0; box-sizing: border-box; }
  html, body { width: 1200px; height: 881px; overflow: hidden; }
  body { background: var(--mat); position: relative; font-family: "Lato", sans-serif; }

  .flyer {
    position: absolute; left: 58px; top: 58px;
    width: 1084px; height: 765px;
    background: var(--paper); overflow: hidden;
  }
  .shapes { position: absolute; inset: 0; width: 1084px; height: 765px; }

  .headline {
    position: absolute; left: 40px; top: 102px;
    font-family: "Barlow Semi Condensed", sans-serif; font-weight: 700;
    color: var(--white); font-size: 61px; line-height: 58px; letter-spacing: 0.3px;
  }
  .subline {
    position: absolute; left: 40px; top: 302px;
    font-family: "Barlow Semi Condensed", sans-serif; font-weight: 700;
    color: var(--white); font-size: 40px; line-height: 39px;
  }

  .offer { position: absolute; left: 40px; top: 456px; color: var(--white); font-weight: 900; }
  .offer .lead, .offer .dates { font-size: 26px; line-height: 32px; }
  .offer .discount { font-size: 41px; line-height: 42px; }
  .offer .url { font-size: 37px; line-height: 46px; font-weight: 700; }

  .brand {
    position: absolute; left: 40px; top: 652px;
    display: flex; align-items: center; gap: 26px;
  }
  .brand-dot { width: 42px; height: 42px; border-radius: 50%; background: var(--navy); }
  .brand-name { color: var(--navy); font-size: 26px; line-height: 30px; font-weight: 400; letter-spacing: 0.3px; }

  .salary {
    position: absolute; right: 22px; top: 656px; text-align: right;
    color: var(--white); font-weight: 900; font-size: 24px; line-height: 31px;
  }
</style>
</head>
<body>
  <section class="flyer">
    <svg class="shapes" viewBox="0 0 1084 765" aria-hidden="true">
      <polygon class="sky-block" fill="var(--sky)" points="694,134 1084,134 1084,518 520,518 542,442 262,442 274,422 626,422" />
      <polygon class="slate-panel" fill="var(--slate)" points="0,442 560,442 502,638 0,638" />
      <polygon class="navy-band" fill="var(--navy)" points="0,66 668,66 534,422 0,422" />
      <polygon class="navy-fold" fill="var(--navy-fold)" points="668,66 694,134 642,134" />
    </svg>

    <svg class="shapes dean-photo" viewBox="0 0 1084 765" role="img" aria-label="Portrait photo of the school's dean, smiling young man with glasses in a white shirt">
      <defs>
        <linearGradient id="deanTone" x1="0" y1="0" x2="0" y2="1">
          <stop offset="0" stop-color="var(--skin)" />
          <stop offset="0.6" stop-color="var(--skin)" />
          <stop offset="0.75" stop-color="var(--shirt)" />
          <stop offset="1" stop-color="var(--shirt)" />
        </linearGradient>
      </defs>
      <path fill="url(#deanTone)" d="M410,765 L470,470 L690,420 L690,20 L1010,20 L1010,420 L1084,470 L1084,765 Z" />
    </svg>

    <svg class="shapes" viewBox="0 0 1084 765" aria-hidden="true">
      <polygon class="salary-band" fill="var(--navy)" points="658,742 682,640 1084,640 1084,742" />
    </svg>

    <h1 class="headline">LEARN EUROPEAN<br>PROGRAMMING<br>COURSES IN BEKASI</h1>
    <p class="subline">3 MONTH MODULES FROM<br>BEGINNER TO ADVANCED</p>

    <div class="offer">
      <p class="lead">ATTEND FREE CLASS &amp; GET</p>
      <p class="discount">10% OFF COURSE,</p>
      <p class="dates">SIGN UP BETWEEN 7-18 MARCH</p>
      <p class="url">vantrel.example/free</p>
    </div>

    <div class="brand">
      <span class="brand-dot"></span>
      <p class="brand-name">VANTREL ACADEMY<br>OF COMPUTING</p>
    </div>

    <p class="salary">GRADUATE AND GET HIRED TO<br>EARN 120 MILLION IDR/YEAR</p>
  </section>
</body>
</html>
```